The calm within me tour 2019

I need an improvement of my own design for a speaking tour on shame and mental health. The advertisement will be for social media. I would like someone to remove the background and do something creative and contemporary. My preference is just my head and shoulders.

Target Market(s)

Church pastors and leaders of mental health organisations

Industry/Entity Type

Mental Health

Requirements
Must have
• The same wording as original
• Delete background and replace with something that is simple but funky

```html
<!DOCTYPE html>
<html lang="en">
<head>
<meta charset="utf-8">
<title>The calm within me tour 2019</title>
<link href="https://fonts.googleapis.com/css2?family=Roboto:ital,wght@0,400;0,700;1,900&family=Roboto+Condensed:ital,wght@1,700&display=swap" rel="stylesheet">
<style>
  :root {
    --orange: #ff9500;
    --orange-stripe: #ff9a0a;
    --yellow: #ffff00;
    --grey-text: #8f8f8f;
    --blue: #5b84e8;
    --link-blue: #4f8df5;
    --white: #ffffff;
    --photo-light: #b9b9b9;
    --photo-dark: #1e1e1e;
  }
  html, body { margin: 0; padding: 0; overflow: hidden; background: var(--orange); }
  .poster {
    position: relative;
    width: 800px;
    height: 1200px;
    overflow: hidden;
    background: var(--orange);
    font-family: "Roboto", Arial, sans-serif;
  }
  .top-band { position: absolute; left: 0; top: 0; width: 800px; height: 14px; background: var(--yellow); }
  .bottom-band { position: absolute; left: 0; bottom: 0; width: 150px; height: 8px; background: var(--blue); }
  .backdrop-grid, .portrait, .stripes { position: absolute; left: 0; top: 0; }
  .headline {
    position: absolute; left: 88px; top: 70px; margin: 0;
    font: italic 900 104px/150px "Roboto", Arial, sans-serif;
    color: var(--yellow); letter-spacing: -1px;
  }
  .quote {
    position: absolute; left: 98px; top: 575px; margin: 0;
    font: italic 700 36px/58px "Roboto Condensed", Arial, sans-serif;
    color: var(--grey-text);
  }
  .quote .emph { color: var(--white); }
  .brand {
    position: absolute; left: 258px; top: 1082px;
    display: flex; flex-direction: column; align-items: center; gap: 6px;
  }
  .brand-mark { width: 46px; height: 46px; background: var(--blue); border-radius: 8px; }
  .brand-name { font: 700 16px/1 "Roboto", Arial, sans-serif; color: var(--blue); }
  .brand-info { position: absolute; left: 388px; top: 1088px; font: 700 17px/19px "Roboto", Arial, sans-serif; color: var(--white); }
  .brand-url { position: absolute; left: 388px; top: 1142px; font: 400 28px/1 "Roboto", Arial, sans-serif; color: var(--link-blue); }
</style>
</head>
<body>
<main class="poster">
  <div class="top-band"></div>

  <svg class="backdrop-grid" width="800" height="1200" viewBox="0 0 800 1200" aria-hidden="true">
    <g fill="#ffffff" opacity="0.18">
      <rect x="74" y="66" width="100" height="100"/><rect x="180" y="66" width="100" height="100"/>
      <rect x="286" y="66" width="100" height="100"/><rect x="392" y="66" width="100" height="100"/>
      <rect x="74" y="172" width="100" height="100"/><rect x="180" y="172" width="100" height="100"/>
      <rect x="286" y="172" width="100" height="100"/><rect x="392" y="172" width="100" height="100"/>
      <rect x="74" y="278" width="100" height="100"/><rect x="180" y="278" width="100" height="100"/>
      <rect x="286" y="278" width="100" height="100"/><rect x="392" y="278" width="100" height="100"/>
      <rect x="74" y="384" width="100" height="100"/><rect x="286" y="384" width="100" height="100"/>
      <rect x="392" y="384" width="100" height="100"/>
      <polygon points="500,66 610,66 680,166 610,266 500,266 570,166"/>
      <polygon points="500,384 610,384 700,484 610,560 520,560 590,484"/>
    </g>
  </svg>

  <svg class="portrait" width="800" height="1200" viewBox="0 0 800 1200">
    <defs>
      <linearGradient id="portrait-tone" x1="0" y1="0" x2="0" y2="1">
        <stop offset="0" stop-color="var(--photo-light)"/>
        <stop offset="0.45" stop-color="#6d6d6d"/>
        <stop offset="1" stop-color="var(--photo-dark)"/>
      </linearGradient>
    </defs>
    <path role="img" aria-label="Photo of the speaker in a black V-neck t-shirt, head and shoulders, black and white"
          d="M520 540 Q528 470 592 468 Q662 470 672 540 Q684 600 664 660 L658 712 Q760 740 800 770 L800 1200 L440 1200 L452 820 Q480 745 552 722 L540 668 Q514 608 520 540 Z"
          fill="url(#portrait-tone)"/>
  </svg>

  <svg class="stripes" width="800" height="1200" viewBox="0 0 800 1200" aria-hidden="true">
    <g fill="var(--orange-stripe)">
      <polygon points="380,960 800,780 800,804 380,984"/>
      <polygon points="400,1030 800,858 800,882 400,1054"/>
      <polygon points="420,1100 800,938 800,962 420,1124"/>
      <polygon points="600,1130 800,1040 800,1064 600,1154"/>
    </g>
  </svg>

  <h1 class="headline">The calm<br>within me<br>tour 2019</h1>

  <p class="quote">“You can’t<br>tell just by<br>looking at<br>someone<br>what they<br>are dealing<br>with <span class="emph">inside.”</span></p>

  <div class="brand">
    <span class="brand-mark"></span>
    <span class="brand-name">dan hollis</span>
  </div>
  <div class="brand-info">Dan Hollis<br>Calm within me</div>
  <div class="brand-url">www.danhollis.co</div>

  <div class="bottom-band"></div>
</main>
</body>
</html>
```